International Food Manufacturer in the need of a new business card and logo.

Our Company - Northgate Pantry Ltd.

Our Industry - Food and Drink

We are a Wild Harvested Food Distributor / Manufacturer. We service the following food sectors: Supermarkets, Hotels, Restaurants, Cafes, Catering and all people looking to eat healthy food products.

Slogan - The foremost source for everything healthy

Business card details -

48-52 Marlow Lane
Hatherby Green
London
EC9Z 4RT United Kingdom
Dennis Prowle
+44 7000 481736 - UK
+971 50 7739205 - UAE
+38 063 914 2758 - Ukraine
dennis@northgatepantry.example
www.northgatepantry.example

Goal - We are looking for a dynamic modern new look for our corporate image and a designer who can bring this new concept to our future food product designs. Please try to incorporate 3d hexagonal vector Imaging in your design concepts.

Target Market(s)

Industry/Entity Type

Food Service

Contact Information for Business Card

Northgate Pantry Ltd.
48-52 Marlow Lane
Hatherby Green
London
EC9Z 4RT United Kingdom
Dennis Prowle
+44 7000 481736 - UK
+971 50 7739205 - UAE

Font styles to use
Serif

Colors

Designer to choose colors to be used in the design.

Requirements
Must have
• Please read project description above.
Nice to have
Should not have

```html
<!DOCTYPE html>
<html lang="en">
<head>
<meta charset="utf-8">
<title>Northgate Pantry Ltd. — Business Card</title>
<link rel="stylesheet" href="https://fonts.googleapis.com/css2?family=Montserrat:wght@800&family=Roboto:wght@300;400&display=swap">
<style>
  :root{
    --stage:#e4e4e6;
    --ink:#262626;
    --panel-light:#eceef2;
    --panel-mid:#d9dce2;
    --accent:#1a80c0;
    --paper:#ffffff;
  }
  html,body{margin:0;padding:0;width:1200px;height:1097px;overflow:hidden;background:var(--stage);}
  .card{
    position:absolute;left:100px;top:262px;width:1000px;height:572px;
    background:var(--ink);overflow:hidden;
    font-family:"Roboto",Arial,sans-serif;color:var(--paper);
    box-shadow:0 10px 30px rgba(0,0,0,.18);
  }
  .hex-panel{
    position:absolute;inset:0;
    background:radial-gradient(ellipse at 62% 55%, #ffffff 0%, var(--panel-light) 40%, var(--panel-mid) 100%);
    clip-path:polygon(0 250px,700px 250px,700px 140px,1000px 140px,1000px 335px,110px 335px,110px 400px,0 400px);
  }
  .brand{
    position:absolute;right:48px;top:52px;display:flex;align-items:center;gap:14px;
    font-weight:300;font-size:26px;letter-spacing:.5px;color:var(--paper);
  }
  .brand-mark{width:32px;height:32px;background:var(--accent);}
  .person{position:absolute;left:46px;top:128px;}
  .person-name{
    margin:0;font-family:"Montserrat",Arial,sans-serif;font-weight:800;
    font-size:60px;line-height:1;letter-spacing:1px;text-transform:uppercase;
  }
  .slogan{margin:12px 0 0 4px;font-weight:300;font-size:23px;letter-spacing:.5px;}
  .contact{position:absolute;left:0;top:346px;width:100%;}
  .row{position:absolute;display:flex;align-items:center;gap:9px;font-weight:300;font-size:21px;white-space:nowrap;}
  .row-phone{left:128px;top:0;}
  .row-address{left:158px;top:54px;}
  .row-web{left:188px;top:108px;}
  .icon{width:38px;height:38px;background:var(--accent);display:flex;align-items:center;justify-content:center;flex:none;}
  .icon svg{width:22px;height:22px;}
  .num{background:var(--accent);padding:2px 7px;}
  .label{margin-left:3px;}
  .email{display:flex;align-items:center;gap:10px;margin-left:30px;}
</style>
</head>
<body>
  <article class="card">
    <div class="hex-panel" role="img" aria-label="Soft white 3D hexagon relief pattern"></div>

    <div class="brand"><span>Northgate Pantry Ltd.</span><span class="brand-mark"></span></div>

    <header class="person">
      <h1 class="person-name">Dennis Prowle</h1>
      <p class="slogan">The foremost source for everything healthy</p>
    </header>

    <section class="contact">
      <div class="row row-phone">
        <span class="icon"><svg viewBox="0 0 24 24" fill="#fff"><path d="M6.6 10.8a15 15 0 0 0 6.6 6.6l2.2-2.2c.3-.3.7-.4 1-.2 1.1.4 2.3.6 3.6.6.6 0 1 .4 1 1V20c0 .6-.4 1-1 1A17 17 0 0 1 3 4c0-.6.4-1 1-1h3.5c.6 0 1 .4 1 1 0 1.3.2 2.5.6 3.6.1.3 0 .7-.2 1z"/></svg></span>
        <span class="label">UK</span><span class="num">+44 7000 481736</span>
        <span class="label">UAE</span><span class="num">+971 50 7739205</span>
        <span class="label">Ukraine</span><span class="num">+38 063 914 2758</span>
      </div>
      <div class="row row-address">
        <span class="icon"><svg viewBox="0 0 24 24" fill="#fff"><path d="M12 2a7 7 0 0 0-7 7c0 5 7 13 7 13s7-8 7-13a7 7 0 0 0-7-7zm0 9.5A2.5 2.5 0 1 1 12 6.5a2.5 2.5 0 0 1 0 5z"/></svg></span>
        <span>48-52 Marlow Lane, Hatherby Green, London, EC9Z 4RT United Kingdom</span>
      </div>
      <div class="row row-web">
        <span class="icon"><svg viewBox="0 0 24 24" fill="none" stroke="#fff" stroke-width="1.6"><circle cx="12" cy="12" r="9"/><path d="M3 12h18M12 3c3 3 3 15 0 18M12 3c-3 3-3 15 0 18"/></svg></span>
        <span>www.northgatepantry.example</span>
        <span class="email">
          <span class="icon"><svg viewBox="0 0 24 24" fill="#fff"><path d="M3 6h18v12H3z"/><path d="M3 6l9 7 9-7" stroke="#1a80c0" stroke-width="1.6" fill="none"/></svg></span>
          <span>dennis@northgatepantry.example</span>
        </span>
      </div>
    </section>
  </article>
</body>
</html>
```